Online Rug Store needs Clearance Banner

Website is: Lanternfield Carpets and Home
You can access it at: www.lanternfieldcarpetsandhome.com and login (top right) with password: trazok

*** update: When creating banners for my site, you have permission to use images from www.velbora.com, but ONLY for this project. The images/artwork are copyright allowable for use on www.lanternfieldcarpetsandhome.com projects.***

We need a home page banner sized 1000 wide x 500 tall pixels to promote a "Clearance Sale" on rugs. The banner can state:

1. Clearance Sale
2. Now in progress
3. Save an extra 20% with coupon code 'Mint20'
4. Ends March 31st
5. Plus Free Shipping and 30 day returns.

We prefer a banner that appears hand-drawn and artistic, not commercially produced. It is OK to use a room scene image, rug images, or just a colored/textured background with text and no images. Your choice.

Flat graphics with no shadows and 3-D effect preferred.
Attached is are 3 logo options, as well as an example banner with handcrafted, artistic styling that we prefer.

Target Market(s)

This should be an eye-catching banner to showcase a very urgent promotion. Consider using colors of red, white, gold, and black to make a strong statement on the home page.

Industry/Entity Type

Home And Garden

Requirements
Must have
• Winner must provide Photoshop editable file format (.psd format) including layers that can be edited.
Nice to have
• Hand-drawn, stenciled, scribbled, artistic graphics and fonts is nice because we sell rugs that are made by hand.
Should not have
• little to no shadowing. Avoid computerized graphics.

```html
<!DOCTYPE html>
<html lang="en">
<head>
<meta charset="utf-8">
<title>Clearance Sale Banner – Lanternfield Carpets and Home</title>
<link rel="stylesheet" href="https://fonts.googleapis.com/css2?family=Arimo:wght@700&family=Cinzel:wght@400;500&display=swap">
<style>
  :root {
    --room-light: #d9c6a8;
    --room-mid: #9b7a55;
    --room-dark: #4a2f1d;
    --rug-navy: #17161f;
    --rug-brown: #6b3f22;
    --rug-cream: #d8c7a4;
    --band-white: rgba(255, 255, 255, 0.84);
    --sale-red: #e0141c;
    --headline-dark: #24170f;
    --white: #ffffff;
  }
  html, body {
    margin: 0;
    padding: 0;
    width: 1200px;
    height: 600px;
    overflow: hidden;
    background: #ffffff;
  }
  .banner {
    position: relative;
    width: 1200px;
    height: 600px;
    overflow: hidden;
  }
  .backdrop {
    position: absolute;
    inset: 0;
    width: 1200px;
    height: 600px;
  }
  .brand {
    position: absolute;
    left: 18px;
    top: 18px;
    width: 282px;
    height: 76px;
    background: var(--white);
    display: flex;
    align-items: center;
    gap: 12px;
    padding: 0 14px;
    box-sizing: border-box;
  }
  .brand-mark {
    width: 44px;
    height: 44px;
    flex: none;
    background: var(--sale-red);
  }
  .brand-name {
    font-family: "Cinzel", serif;
    font-weight: 400;
    font-size: 19px;
    line-height: 1.15;
    color: var(--headline-dark);
  }
  .headline-band {
    position: absolute;
    left: 0;
    top: 174px;
    width: 1200px;
    height: 252px;
    background: var(--band-white);
  }
  .headline {
    position: absolute;
    left: 0;
    top: 186px;
    width: 1200px;
    margin: 0;
    text-align: center;
    white-space: nowrap;
    font-family: "Arimo", sans-serif;
    font-weight: 700;
    font-size: 154px;
    line-height: 1;
    letter-spacing: -2px;
    word-spacing: 28px;
    color: var(--headline-dark);
  }
  .end-date {
    position: absolute;
    left: 0;
    top: 336px;
    width: 1200px;
    margin: 0;
    text-align: center;
    white-space: nowrap;
    font-family: "Cinzel", serif;
    font-weight: 400;
    font-size: 62px;
    line-height: 1;
    color: var(--sale-red);
  }
  .end-date sup {
    font-size: 30px;
    vertical-align: 26px;
  }
  .offer-band {
    position: absolute;
    left: 0;
    top: 450px;
    width: 1200px;
    height: 126px;
    background: var(--sale-red);
    color: var(--white);
    font-family: "Cinzel", serif;
    text-align: center;
    white-space: nowrap;
  }
  .offer-code {
    margin: 16px 0 0;
    font-size: 38px;
    font-weight: 400;
    line-height: 1.1;
    letter-spacing: 1px;
  }
  .offer-perks {
    margin: 12px 0 0;
    font-size: 30px;
    font-weight: 400;
    letter-spacing: 3px;
    word-spacing: 4px;
  }
  .perk-sep {
    display: inline-block;
    margin: 0 28px;
    font-size: 22px;
    vertical-align: 4px;
  }
</style>
</head>
<body>
  <main class="banner">
    <svg class="backdrop" viewBox="0 0 1200 600" xmlns="http://www.w3.org/2000/svg">
      <defs>
        <linearGradient id="roomTone" x1="0" y1="0" x2="0.3" y2="1">
          <stop offset="0" stop-color="#8a7055"/>
          <stop offset="0.35" stop-color="var(--room-light)"/>
          <stop offset="0.7" stop-color="var(--room-mid)"/>
          <stop offset="1" stop-color="var(--room-dark)"/>
        </linearGradient>
        <radialGradient id="rugTone" cx="0.55" cy="0.45" r="0.75">
          <stop offset="0" stop-color="var(--rug-navy)"/>
          <stop offset="0.45" stop-color="#3a2418"/>
          <stop offset="0.75" stop-color="var(--rug-brown)"/>
          <stop offset="1" stop-color="var(--rug-cream)"/>
        </radialGradient>
      </defs>
      <polygon points="0,0 708,0 606,600 0,600" fill="url(#roomTone)" role="img" aria-label="Photo of a bright living room with sofa, curtains and a rug on a wood floor"/>
      <polygon points="708,0 1200,0 1200,600 606,600" fill="url(#rugTone)" role="img" aria-label="Close-up photo of a navy and cream Persian-style floral rug"/>
    </svg>

    <div class="brand">
      <span class="brand-mark"></span>
      <span class="brand-name">Lanternfield<br>Carpets and Home</span>
    </div>

    <div class="headline-band"></div>
    <h1 class="headline">Clearance Sale</h1>
    <p class="end-date">Ends March 31<sup>st</sup></p>

    <section class="offer-band">
      <p class="offer-code">SAVE AN EXTRA 20% WITH COUPON CODE 'MINT20'</p>
      <p class="offer-perks">FREE SHIPPING<span class="perk-sep">*</span>30 DAY RETURNS<span class="perk-sep">*</span>NOW IN PROGRESS</p>
    </section>
  </main>
</body>
</html>
```